Realtor needs 8 1/2 x 11 flyer designed both sides

I uploaded a new word doc to be used under each of the pictures on the front page.

Colors

Designer to choose colors to be used in the design.

```html
<!DOCTYPE html>
<html lang="en">
<head>
<meta charset="utf-8">
<title>Agent Transition Flyer</title>
<link rel="stylesheet" href="https://fonts.googleapis.com/css2?family=Nunito:wght@400;800&display=swap">
<style>
  :root {
    --ink: #222426;
    --body: #4a4c4f;
    --brand-blue: #0a5fd6;
    --deep-blue: #0052cc;
    --sky: #cfe9fb;
    --mist: #eceeee;
    --paper: #ffffff;
    --band: #e3e4e5;
  }
  * { margin: 0; padding: 0; box-sizing: border-box; }
  html, body { width: 928px; height: 1200px; overflow: hidden; background: var(--paper); }
  .flyer {
    position: relative;
    width: 928px;
    height: 1200px;
    overflow: hidden;
    font-family: "Nunito", sans-serif;
    background: linear-gradient(180deg, var(--paper) 60%, #f6f6f6 100%);
  }
  .hero { position: absolute; left: 0; top: 0; }
  .agent-card { position: absolute; top: 538px; color: var(--ink); }
  .agent-card--left { left: 38px; text-align: left; }
  .agent-card--right { right: 40px; text-align: right; }
  .agent-name { font-weight: 800; font-size: 27px; line-height: 32px; letter-spacing: 0.2px; }
  .agent-name .surname { color: var(--brand-blue); }
  .agent-phone { font-size: 20px; line-height: 26px; margin-top: 2px; }
  .agent-phone sup { font-size: 9px; vertical-align: 9px; }
  .agent-contact { font-size: 17.5px; line-height: 22px; }
  .letter {
    position: absolute;
    top: 658px;
    color: var(--body);
    font-size: 15.2px;
    line-height: 23.3px;
  }
  .letter p + p { margin-top: 8.6px; }
  .letter--left { left: 39px; width: 392px; }
  .letter--right { left: 459px; width: 432px; }
  .footer-band { position: absolute; left: 0; bottom: 0; }
</style>
</head>
<body>
<main class="flyer">
  <svg class="hero" width="928" height="540" viewBox="0 0 928 540">
    <defs>
      <linearGradient id="heroPhoto" x1="0" y1="0" x2="1" y2="1">
        <stop offset="0" stop-color="#d9b57a"/>
        <stop offset="0.35" stop-color="#7a8ea6"/>
        <stop offset="0.7" stop-color="#a9b6c4"/>
        <stop offset="1" stop-color="#6f9a4e"/>
      </linearGradient>
      <linearGradient id="silverRing" x1="0" y1="0" x2="1" y2="1">
        <stop offset="0" stop-color="#6d6f72"/>
        <stop offset="0.3" stop-color="#f4f4f4"/>
        <stop offset="0.55" stop-color="#9a9c9f"/>
        <stop offset="0.8" stop-color="#ffffff"/>
        <stop offset="1" stop-color="#5e6063"/>
      </linearGradient>
      <linearGradient id="portraitTone" x1="0" y1="0" x2="0" y2="1">
        <stop offset="0" stop-color="#c9a98a"/>
        <stop offset="0.45" stop-color="#8a6e5c"/>
        <stop offset="1" stop-color="#1e1c1e"/>
      </linearGradient>
    </defs>
    <rect class="backdrop" width="928" height="540" fill="var(--paper)"/>
    <path class="backdrop-mist" d="M0 0 H928 V470 C820 460 700 470 620 450 C500 500 360 540 220 520 C120 505 50 470 0 440 Z" fill="var(--mist)"/>
    <path class="sky-panel" d="M560 90 C650 60 760 40 928 40 V360 C830 330 700 360 600 410 Z" fill="var(--sky)"/>
    <path class="swoosh-upper" d="M430 150 C560 40 720 0 928 0 V40 C760 50 640 70 540 140 C500 170 470 190 430 210 Z" fill="var(--deep-blue)"/>
    <path class="swoosh-lower" d="M480 440 C600 350 760 190 928 200 V370 C780 330 640 400 500 460 Z" fill="var(--deep-blue)"/>
    <path class="swoosh-grey" d="M400 120 C470 70 520 55 560 58 C500 80 460 110 430 140 Z" fill="#cfd1d3"/>
    <path class="hero-photo" role="img" aria-label="Photo of the incoming agent in a dark blazer standing before a blue two-storey house with a garage and porch"
      d="M0 195 C150 110 380 50 580 62 C610 140 640 290 615 372 C540 450 400 525 250 522 C150 520 60 480 0 440 Z" fill="url(#heroPhoto)"/>
    <circle class="portrait-ring" cx="803" cy="374" r="154" fill="url(#silverRing)"/>
    <circle class="portrait-rim" cx="803" cy="374" r="154" fill="none" stroke="#55575a" stroke-width="2"/>
    <circle class="portrait-photo" role="img" aria-label="Portrait of the retiring agent seated in a black top with a beaded necklace" cx="803" cy="374" r="138" fill="url(#portraitTone)"/>
  </svg>

  <section class="agent-card agent-card--left">
    <h2 class="agent-name">DANA <span class="surname">MORETTI</span></h2>
    <p class="agent-phone">555-214-3860 &nbsp;|&nbsp; Realtor<sup>®</sup></p>
    <p class="agent-contact">Dana@DanaMHomes.com</p>
    <p class="agent-contact">DRE# 01873264</p>
  </section>

  <section class="agent-card agent-card--right">
    <h2 class="agent-name">HELENA <span class="surname">WARD</span></h2>
    <p class="agent-phone">555-478-2019 &nbsp;|&nbsp; Realtor<sup>®</sup></p>
    <p class="agent-contact">Helena@HelenaWard.com</p>
    <p class="agent-contact">DRE# 00641978</p>
  </section>

  <article class="letter letter--left">
    <p>Know many of you, but for those whom I do not, I’d like to introduce myself. I’ve been a resident of Harbor Crest for almost 23 years now. I’ve loved our neighborhood from the first time I discovered it. From our beautiful parks to our fabulous pool and amenities., it’s hard to beat our wonderful community.</p>
    <p>I always say where we live is the next best thing to living on a tropical island. I’ve traveled to many and I’m always happy to come back to my Harbor Crest home My passion for this area is why I’m in Real Estate. I consider myself incredibly fortunate to sell homes and help people purchase homes in an area that I love with all my heart.</p>
    <p>Helena and I have been close colleagues for the last 8 years, both working as Realtors and long time residents of Harbor Crest. I am most grateful for our working relationship and the friendship we have formed. I am humbled by her trust and respect for me. Please feel welcome to call on me for all things home-related. I will look forward to meeting you!</p>
  </article>

  <article class="letter letter--right">
    <p>I have exciting and bittersweet news I want to share with my Harbor Crest clients, friends and neighbors. After 40 (something) years in the Real Estate business, I have decided to retire. Some of you may last month I sold my Harbor Crest home and moved to the beautiful Willow Terrace community in Canyon Vista. My husband and I wanted to scale down and have time to enjoy retirement, together. I have been so blessed to have had an illustrious career in Real Estate and I want to thank you with a most grateful heart for heart for giving me the opportunity to work with you. I have enjoyed every minute.</p>
    <p>I’m happy and proud to be turning my business over to Dana Moretti, fellow Summit Realty agent. She and I have enjoyed a very close working relationship for many years and there is nobody else except Dana is...I will add verbiage here conveying your thoughts about me. Please contact me if you’d like a personal introducing to Dana or contact her directly. Remember to mention me when you contact Dana and let her know that we know. each other. I wish you the very best and please say hello when you see me in the neighborhood.</p>
  </article>

  <svg class="footer-band" width="928" height="50" viewBox="0 0 928 50">
    <path d="M0 22 C300 10 650 8 928 14 V50 H0 Z" fill="var(--band)"/>
  </svg>
</main>
</body>
</html>
```